We need to a website for a contact center that provides answering services by voice and chat.

A similar website in terms of design is the following site:
http://www.brindlequay.example/

The colors and look and feel should be different and creative but the structure should be similar to the above mentioned website.

Attached is the text file.

The design should communicate professionalism and friendly customer service oriented company. The visitor to the site must have a feel that "this company looks professional and they will take care of my client."

I am looking for design only, but if the designer will also do the coding, it will be an advantage.

Target Market(s)

Our target market are lawyers and doctors who require someone to answer their clients calls 24/7.

Industry/Entity Type

It Company

Requirements
Nice to have
• Since the company is based in Dubai, the website should reflect the Middle East people not pure European or pure Asians. A mixture of nationalities is fine to be visible in the pictures but it must include at least an arab or middle eastern person.
Should not have
• No old style, Times Roman font, do not include illustrations or cartoon graphics or pictures that are very common or widely used.

```html
<!DOCTYPE html>
<html lang="en">
<head>
<meta charset="utf-8">
<title>Cedar Line – Business Call Center &amp; Live Answering Service</title>
<link rel="stylesheet" href="https://fonts.googleapis.com/css2?family=Open+Sans:wght@300;400;600&family=Ubuntu:wght@400;500;700&display=swap">
<style>
:root{
  --brand-red:#7e2b22;
  --brand-red-dark:#5e1d16;
  --ink:#3f4560;
  --text:#3a3a3a;
  --page:#ffffff;
  --header-bg:#f8f8f8;
  --topbar:#ececec;
  --login:#353a4e;
  --footer:#464646;
  --footer-text:#d9d9d9;
  --panel:#ebebeb;
}
*{box-sizing:border-box;margin:0;padding:0}
html,body{width:1016px;height:1200px;overflow:hidden;background:var(--page)}
body{font-family:"Open Sans",Arial,sans-serif;color:var(--text);position:relative}
.wrap{position:absolute;left:85px;width:847px}
a{color:inherit;text-decoration:none}

.topbar{position:absolute;top:0;left:0;width:1016px;height:21px;background:var(--topbar)}
.client-login{position:absolute;right:84px;top:0;height:21px;padding:0 11px;background:var(--login);color:#fff;font-size:11px;line-height:21px}

.header{position:absolute;top:21px;left:0;width:1016px;height:109px;background:var(--header-bg)}
.logo{position:absolute;left:85px;top:36px;display:flex;align-items:center;gap:7px;color:var(--brand-red);font-weight:300;font-size:28px;letter-spacing:1px}
.logo .mark{width:12px;height:12px;background:var(--brand-red)}
.tagline{position:absolute;right:84px;top:19px;color:var(--brand-red);font-size:15px}
.pill{position:absolute;top:58px;height:29px;border-radius:14px;background:linear-gradient(#f7f7f7,#dcdcdc);border:1px solid #c9c9c9;font-family:"Ubuntu",sans-serif;font-weight:500;color:#333;display:flex;align-items:center;justify-content:center;gap:6px}
.pill.price{left:589px;width:150px;font-size:13.5px}
.pill.phone{left:748px;width:184px;font-size:17px;font-weight:700}

.nav{top:130px;height:33px;background:var(--brand-red);display:flex}
.nav a{flex:1 1 0;color:#fff;font-size:12px;display:flex;align-items:center;justify-content:center;border-left:1px solid rgba(255,255,255,.18)}
.nav a:first-child{border-left:none;background:var(--ink)}

.hero{top:165px;height:364px}
.hero-photo{position:absolute;inset:0;background:linear-gradient(90deg,#e9e3dc 0%,#d9cbbd 35%,#cdb29a 60%,#c7a88f 80%,#d8cdc3 100%)}
.hero h1{position:absolute;left:15px;top:32px;font-family:"Ubuntu",sans-serif;font-weight:700;font-size:34px;color:var(--ink)}
.hero .sub{position:absolute;left:15px;top:81px;font-size:17px;font-weight:300;color:#333}
.hero .trial{position:absolute;left:15px;top:115px;font-family:"Ubuntu",sans-serif;font-weight:700;font-size:17px;color:var(--brand-red)}
.field{position:absolute;left:17px;width:225px;height:26px;background:#fff;border:1px solid #d6d6d6;font-size:11.5px;color:#333;padding:0 7px;line-height:24px}
.btn-start{position:absolute;left:19px;top:297px;width:99px;height:28px;border-radius:14px;background:linear-gradient(#fff,#dedede);border:1px solid #bbb;font-family:"Ubuntu",sans-serif;font-weight:700;font-size:12px;color:#222;display:flex;align-items:center;justify-content:center}

.features{top:531px;height:88px;background:var(--brand-red);display:flex;padding-left:16px}
.feature{width:280px;display:flex;gap:10px;padding-top:12px}
.feature .ico{width:64px;height:64px;flex:none;border-radius:50%;background:var(--brand-red-dark);border:2px solid #a5473c;display:flex;align-items:center;justify-content:center}
.feature h3{font-family:"Ubuntu",sans-serif;font-weight:700;font-size:16px;color:#fff;margin-top:1px}
.feature p{font-size:9.5px;color:#e0aba4;line-height:12px;margin-top:4px;width:190px}
.feature a{font-size:10px;font-weight:600;color:#fff;text-decoration:underline;display:block;margin-top:3px}

.welcome{top:643px;width:405px}
.section-title{font-family:"Ubuntu",sans-serif;font-weight:400;font-size:22px;color:var(--brand-red)}
.welcome p{font-size:11px;line-height:23.7px;margin-top:10px}
.welcome p + p{margin-top:15px}
.newsletter{position:absolute;top:193px;left:0;width:398px;height:97px;background:var(--panel);border:1px solid #d9d9d9;border-radius:3px;padding:10px 9px}
.newsletter h4{font-weight:400;font-size:15.5px;color:#333}
.newsletter .email{position:absolute;left:11px;top:49px;width:305px;height:26px;background:#fff;border:1px solid #d6d6d6;font-size:8.5px;font-style:italic;color:#888;padding-left:6px;line-height:25px}
.newsletter .submit{position:absolute;left:326px;top:48px;width:63px;height:27px;background:var(--brand-red);border:1px solid var(--brand-red-dark);border-radius:2px;color:#fff;font-size:12.5px;display:flex;align-items:center;justify-content:center}

.benefits{top:643px;left:524px;width:420px}
.benefits ul{list-style:none;margin-top:14px}
.benefits li{position:relative;padding-left:30px;font-size:13px;line-height:26.3px;color:#333}
.benefits li::before{content:"";position:absolute;left:5px;top:11px;width:6px;height:6px;border-radius:50%;background:var(--brand-red)}

.footer{top:969px;height:193px;background:var(--footer);color:var(--footer-text)}
.footer-logo{position:absolute;left:17px;top:86px;display:flex;align-items:center;gap:6px;color:#fff;font-weight:300;font-size:18px;letter-spacing:.5px;white-space:nowrap}
.footer-logo .mark{width:9px;height:9px;background:#fff}
.fcol{position:absolute;top:20px;height:160px}
.divider{position:absolute;top:20px;width:1px;height:160px;background:#525252}
.fcol h5{font-family:"Ubuntu",sans-serif;font-weight:500;font-size:14.5px;color:#fff;margin-bottom:10px;white-space:nowrap}
.fcol a{display:block;font-size:10.5px;line-height:19.5px;white-space:nowrap}
.fcol h5.second{margin-top:14px}
.social a{display:flex;align-items:center;justify-content:space-between;width:97px;line-height:26px}
.social .sq{width:19px;height:19px;border-radius:2px;background:#6f9fcf;flex:none}

.legal{position:absolute;top:1177px;left:85px;width:847px;font-size:9.5px;color:#333;display:flex;justify-content:space-between}
.legal .links span{margin:0 8px}
</style>
</head>
<body>

<div class="topbar"><a class="client-login" href="#">CLIENT LOGIN</a></div>

<header class="header">
  <a class="logo" href="#"><span class="mark"></span>Cedar Line</a>
  <div class="tagline">Business Call Center &amp; Live Answering Service</div>
  <div class="pill price">FROM $2.66 A DAY</div>
  <div class="pill phone">
    <svg width="14" height="14" viewBox="0 0 24 24" aria-hidden="true"><path fill="#fff" stroke="#bbb" d="M6.6 10.8a15 15 0 0 0 6.6 6.6l2.2-2.2a1 1 0 0 1 1-.25 11.4 11.4 0 0 0 3.6.6 1 1 0 0 1 1 1V20a1 1 0 0 1-1 1A17 17 0 0 1 3 4a1 1 0 0 1 1-1h3.5a1 1 0 0 1 1 1c0 1.25.2 2.45.6 3.6a1 1 0 0 1-.25 1z"/></svg>
    1.555.010.2400
  </div>
</header>

<nav class="wrap nav">
  <a href="#">Home</a><a href="#">How It Works</a><a href="#">Industries</a><a href="#">About Us</a><a href="#">Testimonials</a><a href="#">Pricing</a><a href="#">Press Room</a><a href="#">Contact Us</a>
</nav>

<section class="wrap hero">
  <div class="hero-photo" role="img" aria-label="Smiling receptionist wearing a headset in a softly blurred office"></div>
  <h1>Premium Live Receptionist</h1>
  <p class="sub">Route Your Business Calls to any Location</p>
  <p class="trial">14 Day Free Trail</p>
  <div class="field" style="top:158px">Home*</div>
  <div class="field" style="top:203px">Phone*</div>
  <div class="field" style="top:249px">Email*</div>
  <a class="btn-start" href="#">GET STARTED</a>
</section>

<section class="wrap features">
  <div class="feature">
    <div class="ico"><svg width="34" height="30" viewBox="0 0 34 30" aria-hidden="true"><path fill="#fff" d="M2 10h7l9-8v26l-9-8H2z"/><path fill="none" stroke="#fff" stroke-width="2.5" stroke-linecap="round" d="M22 10a7 7 0 0 1 0 10M26 6a12 12 0 0 1 0 18"/></svg></div>
    <div><h3>Listen to a Live Demo</h3><p>Le Lorem Ipsum est simplement du faux texte employé dans la.</p><a href="#">Click Here</a></div>
  </div>
  <div class="feature">
    <div class="ico"><svg width="30" height="30" viewBox="0 0 30 30" aria-hidden="true"><rect x="3" y="5" width="22" height="22" rx="2" fill="none" stroke="#fff" stroke-width="2.5"/><path fill="#fff" d="M10 20l2-6 12-12 4 4-12 12z"/></svg></div>
    <div><h3>Request Pricing</h3><p>Le Lorem Ipsum est simplement du faux texte employé dans la.</p><a href="#">Click Here</a></div>
  </div>
  <div class="feature">
    <div class="ico"><svg width="32" height="32" viewBox="0 0 32 32" aria-hidden="true"><circle cx="16" cy="16" r="11" fill="none" stroke="#fff" stroke-width="2.5"/><rect x="12" y="12" width="8" height="8" fill="#fff"/><circle cx="16" cy="5" r="3" fill="#fff"/><circle cx="6" cy="22" r="3" fill="#fff"/><circle cx="26" cy="22" r="3" fill="#fff"/></svg></div>
    <div><h3>Online Signup</h3><p>Le Lorem Ipsum est simplement du faux texte employé dans la.</p><a href="#">Click Here</a></div>
  </div>
</section>

<section class="wrap welcome">
  <h2 class="section-title">Welcome to Cedar Line</h2>
  <p>Cedar Line is a24/7 call center and live answering service, we provide customized solutions for small, medium, and large organizations.</p>
  <p>Our customized solutions help our clients get the maximum return on their in vestment by capturing more leads and projecting a professional image to their customers, in addition tohuge savings on overhead and labor costs.</p>
  <div class="newsletter">
    <h4>Sign up for our FREE Monthly Newsletter</h4>
    <div class="email">Enter your email address...</div>
    <a class="submit" href="#">Submit</a>
  </div>
</section>

<section class="wrap benefits">
  <h2 class="section-title">10 Ways Your Company Can Benefit:</h2>
  <ul>
    <li>Capture more business &amp; increase profits.</li>
    <li>Save thousands on labor costs.</li>
    <li>Improve your company’s "phone image".</li>
    <li>Streamline your call flow.</li>
    <li>Conduct business 24/7 without the overhead.</li>
    <li>Take advantage of a turn-key, streamlined solution.</li>
    <li>Respond instantaneously to clients and prospects.</li>
    <li>Cedar Line uses the most reliable equipment in the industry.</li>
    <li>Cedar Line selects the right people with the best voices.</li>
    <li>Cedar Line over-staffs receptionists to minimize hold times.</li>
  </ul>
</section>

<footer class="wrap footer">
  <div class="footer-logo"><span class="mark"></span>Cedar Line</div>
  <div class="fcol" style="left:154px"><h5>About Cedar Line</h5><a href="#">CRM</a><a href="#">Analytics</a><a href="#">Automation</a><a href="#">Reselling</a><a href="#">Editions</a><a href="#">Testimonials</a></div>
  <div class="divider" style="left:332px"></div>
  <div class="fcol" style="left:382px"><h5>About Us</h5><a href="#">Schedule A Demo</a><a href="#">Contact Us</a><a href="#">Who We Are</a><a href="#">Case Studies</a><a href="#">Our SEO Side</a></div>
  <div class="divider" style="left:509px"></div>
  <div class="fcol" style="left:549px"><h5>Support</h5><a href="#">Support Community</a><a href="#">Getting Started Guide</a><h5 class="second">Customer</h5><a href="#">Quick Video Tour Of DeskFlow</a></div>
  <div class="divider" style="left:718px"></div>
  <div class="fcol social" style="left:747px"><h5>Social Media</h5><a href="#">Social Page<span class="sq"></span></a><a href="#">Microblog<span class="sq"></span></a><a href="#">Pro Network<span class="sq"></span></a><a href="#">Video Channel<span class="sq" style="background:#ddd"></span></a></div>
</footer>

<div class="legal">
  <div class="links"><a href="#">Sitemap</a><span>|</span><a href="#">Privacy</a><span>|</span><a href="#">Terms &amp; Conditions</a></div>
  <div>© Copyrights 2013 All rights Reserved</div>
</div>

</body>
</html>
```